Freelance Makeup Artist Needing Business Card Design

I am a freelance makeup artist looking for a design for my business cards.
My target audience is people looking for bridal makeup, so i was thinking minimalistic style, black with white or gold foil accents.
Something that feels classy but simple and to the point.

I would like the front to state Naomi Carrow and Makeup Artist, and the back to include my social media and contact details.

Target Market(s)

Brides, young women

Industry/Entity Type

Business

Contact Information for Business Card

0417293846
naomi.carrow@mailvista.com
www.snapgrid.com/naomi.carrow
www.friendpage.com/NaomiCarrowMakeup

Requirements
Nice to have
• Social media icons next to relevant contact details

```html
<!DOCTYPE html>
<html lang="en">
<head>
<meta charset="utf-8">
<title>Naomi Carrow — Business Card</title>
<link rel="stylesheet" href="https://fonts.googleapis.com/css2?family=Montserrat:wght@300;400;500&display=swap">
<style>
  :root {
    --backdrop: #9a9a9a;
    --card-black: #050505;
    --card-frame: #232323;
    --ink-white: #ffffff;
    --ink-grey: #9c9c9c;
    --rule-grey: #4a4a4a;
  }
  * { margin: 0; padding: 0; box-sizing: border-box; }
  html, body {
    width: 1200px;
    height: 1000px;
    overflow: hidden;
    background: var(--backdrop);
  }
  .canvas {
    position: relative;
    width: 1200px;
    height: 1000px;
    font-family: "Montserrat", sans-serif;
  }
  .card {
    position: absolute;
    left: 300px;
    width: 600px;
    height: 350px;
    color: var(--ink-white);
    text-align: center;
  }
  .card--front {
    top: 123px;
    background: var(--card-frame);
  }
  .card--front .card__panel {
    position: absolute;
    left: 45px;
    top: 42px;
    width: 510px;
    height: 268px;
    background: var(--card-black);
  }
  .card--back {
    top: 520px;
    background: var(--card-black);
  }
  .brand-mark {
    position: absolute;
    left: 0;
    right: 0;
    font-weight: 300;
    font-size: 22px;
    letter-spacing: 2px;
    line-height: 1;
    color: var(--ink-white);
  }
  .card--front .brand-mark { top: 69px; }
  .card--back .brand-mark { top: 111px; }
  .brand-name {
    position: absolute;
    left: 0;
    right: 0;
    top: 142px;
    font-weight: 400;
    font-size: 31px;
    letter-spacing: 4px;
    line-height: 1.2;
    text-transform: uppercase;
  }
  .brand-rule {
    position: absolute;
    left: 63px;
    right: 63px;
    top: 189px;
    height: 1px;
    background: var(--rule-grey);
  }
  .brand-role {
    position: absolute;
    left: 0;
    right: 0;
    top: 199px;
    font-weight: 300;
    font-size: 20px;
    letter-spacing: 6px;
    color: var(--ink-grey);
    text-transform: uppercase;
    word-spacing: 12px;
  }
  .contact-list {
    position: absolute;
    left: 0;
    right: 0;
    top: 234px;
    list-style: none;
    font-weight: 400;
    font-size: 13px;
    line-height: 16px;
  }
</style>
</head>
<body>
<main class="canvas">
  <section class="card card--front" aria-label="Card front">
    <div class="card__panel">
      <div class="brand-mark">Naomi Carrow</div>
      <h1 class="brand-name">Naomi Carrow</h1>
      <div class="brand-rule"></div>
      <p class="brand-role">Makeup Artist</p>
    </div>
  </section>

  <section class="card card--back" aria-label="Card back">
    <div class="brand-mark">Naomi Carrow</div>
    <ul class="contact-list">
      <li>0417293846</li>
      <li>naomi.carrow@mailvista.com</li>
      <li>www.snapgrid.com/naomi.carrow</li>
      <li>www.friendpage.com/NaomiCarrowMakeup</li>
    </ul>
  </section>
</main>
</body>
</html>
```